Walking Beside the Quiet River; A Study of Refuge, Purpose & Calling

I need a book cover, for the above book title. This is a journey of the heart to know the heart of God. I think on the text, Simple (see below graphic)
Black Lettering for Knowing.....Intimately
Gold lettering for God
Either gold or black for the subtitle; A Study of Refuge, Purpose, & Calling
I would like the below graphic idea only no photograph of a person,
and White background instead of black
Simple Font, like below graphic, but open to suggestions

Target Market(s)

not age specific, Every person has been given a heart to know God, we are taking the mystery out the process to understand God is Father, loving gracious, ever present, etc. If we know His heart, we realize He's not at a distance, He is there, an ever present help

Industry/Entity Type

Security

Requirements
Must have
• Title: Walking Beside the Quiet River; A Study of Refuge, Purpose, & Calling
• My name, Tom Pettigrew
Nice to have
• See Below Graphic

```html
<!DOCTYPE html>
<html lang="en">
<head>
<meta charset="utf-8">
<title>Walking Beside the Quiet River – Book Spine</title>
<link rel="stylesheet" href="https://fonts.googleapis.com/css2?family=Libre+Franklin:wght@700;800&display=swap">
<style>
  :root {
    --ink: #333333;
    --gold: #d4ae3a;
    --paper: #ffffff;
    --spine-fill: #fcfcfc;
    --spine-edge: #e6e6e6;
    --mark: #333333;
  }
  html, body {
    margin: 0;
    padding: 0;
    width: 1200px;
    height: 552px;
    overflow: hidden;
    background: var(--paper);
  }
  .spine-sheet {
    display: block;
    width: 1200px;
    height: 552px;
    font-family: "Libre Franklin", "Franklin Gothic Medium", Arial, sans-serif;
    font-weight: 700;
  }
  .label { fill: var(--ink); font-size: 23px; letter-spacing: 2.5px; }
  .title { fill: var(--ink); font-size: 35px; font-weight: 800; }
  .title .accent { fill: var(--gold); }
  .subtitle { fill: var(--ink); font-size: 22px; }
  .crop-mark { stroke: var(--mark); stroke-width: 1; }
  .imprint-square { fill: var(--gold); }
  .imprint-name { fill: var(--ink); font-size: 19px; font-weight: 700; letter-spacing: 2px; }
  .spine-panel { fill: var(--spine-fill); stroke: var(--spine-edge); stroke-width: 1; }
</style>
</head>
<body>
<svg class="spine-sheet" viewBox="0 0 1150 530" preserveAspectRatio="xMidYMid meet" xmlns="http://www.w3.org/2000/svg">

  <!-- Spine with trim marks -->
  <g class="spine spine--trim">
    <text class="label" x="556" y="20" text-anchor="middle">BOOK SPINE</text>

    <g class="crop-marks">
      <line class="crop-mark" x1="50.5" y1="38" x2="50.5" y2="62"/>
      <line class="crop-mark" x1="50.5" y1="238" x2="50.5" y2="262"/>
      <line class="crop-mark" x1="1104.5" y1="38" x2="1104.5" y2="62"/>
      <line class="crop-mark" x1="1104.5" y1="238" x2="1104.5" y2="262"/>
      <line class="crop-mark" x1="0" y1="80.5" x2="24" y2="80.5"/>
      <line class="crop-mark" x1="0" y1="222.5" x2="24" y2="222.5"/>
      <line class="crop-mark" x1="1126" y1="80.5" x2="1150" y2="80.5"/>
      <line class="crop-mark" x1="1126" y1="222.5" x2="1150" y2="222.5"/>
    </g>

    <text class="title" x="495" y="145" text-anchor="middle" textLength="832" lengthAdjust="spacing">WALKING BESIDE THE <tspan class="accent">QUIET</tspan> RIVER</text>
    <text class="subtitle" x="495" y="190" text-anchor="middle" textLength="838" lengthAdjust="spacing">A STUDY OF REFUGE, PURPOSE AND CALLING</text>

    <g class="imprint">
      <rect class="imprint-square" x="960" y="143" width="16" height="16"/>
      <text class="imprint-name" x="986" y="158">ALDERWAY</text>
    </g>
  </g>

  <!-- Spine as finished panel -->
  <g class="spine spine--finished">
    <text class="label" x="574" y="325" text-anchor="middle">BOOK SPINE</text>

    <rect class="spine-panel" x="68.5" y="385.5" width="1053" height="142"/>

    <text class="title" x="515" y="450" text-anchor="middle" textLength="832" lengthAdjust="spacing">WALKING BESIDE THE <tspan class="accent">QUIET</tspan> RIVER</text>
    <text class="subtitle" x="515" y="496" text-anchor="middle" textLength="838" lengthAdjust="spacing">A STUDY OF REFUGE, PURPOSE AND CALLING</text>

    <g class="imprint">
      <rect class="imprint-square" x="980" y="449" width="16" height="16"/>
      <text class="imprint-name" x="1006" y="464">ALDERWAY</text>
    </g>
  </g>
</svg>
</body>
</html>
```